FINANCIAL APP design, high image for young generation

We need to re-design the Attached APP. It is a financial APP, therefore the general tone should be serious, but still young (25-45 years old the majority of users)

Images to have clear vision are all attached.
Specifics:
1. We'd like an elegant blue color, somehow brilliant (we're in finance sector).
2. Style should be "financial", even though not old style ma new generation
3. You are required to find a way to give the meaning of this App image (see in Templates attached the Roket taking off, but change image in a real picture). You can choose a nice picture or a very nice design. Propose to your own judgment: we want to give the image os something that is starting a trip to the moon
4.. From n. 1 to n. 6 are all in front page, that scrolls from 1 to 6. User reaches the other ones by clicking and see them full page. Mainly on phone (about 80% of times)
5. Add our Veltrano Orbis logo with an added word: WALLET in clean letters.

Feel free to ask if needed.

Target Market(s)

Financial App

Industry/Entity Type

Financial Service

Font styles to use
Sans Serif

Colors
0456a4

Requirements
Must have
• 1. Financial Status, but young generation
2. A Rocket taking off in front image
3. A deep Sky with moon as a shadow image on other pages (it must be seen but not detailed) Designer can choose anyone In pixelvault-demo.com. We'll buy it or them after approval with his indications
Nice to have
• Logo

```html
<!DOCTYPE html>
<html lang="en">
<head>
<meta charset="utf-8">
<title>Veltrano Orbis Wallet — App Screens</title>
<link rel="stylesheet" href="https://fonts.googleapis.com/css2?family=Montserrat:wght@400;500;600;700&display=swap">
<style>
  :root {
    --stage: #262729;
    --brand-blue: #0456a4;
    --card-blue: #0b63c9;
    --card-blue-deep: #0550b0;
    --tag-blue: #3f8ef2;
    --navy: #1b1a4c;
    --navy-deep: #14123a;
    --accent-violet: #3a2a7a;
    --white: #ffffff;
    --screen-bg: #f4f4f6;
    --ink: #111111;
    --icon-grey: #8a8a90;
    --action-blue: #1f7ad8;
  }
  * { box-sizing: border-box; margin: 0; padding: 0; }
  html, body {
    width: 1200px; height: 796px; overflow: hidden;
    background: var(--stage);
    font-family: "Montserrat", sans-serif;
  }
  .stage {
    position: relative; width: 1200px; height: 796px;
    display: flex; justify-content: center; align-items: center; gap: 80px;
  }
  .screen {
    position: relative; width: 360px; height: 740px;
    border-radius: 44px; overflow: hidden;
  }

  /* Splash screen */
  .splash {
    background: var(--brand-blue);
    display: flex; flex-direction: column; align-items: center; justify-content: center; gap: 18px;
  }
  .splash-mark { display: flex; align-items: center; gap: 14px; }
  .splash-dot { width: 46px; height: 46px; border-radius: 50%; background: var(--white); }
  .splash-name {
    color: var(--white); font-weight: 700; font-size: 26px; line-height: 1.15;
  }

  /* Home screen */
  .home { background: var(--screen-bg); padding: 40px 14px 0; }
  .feature-card {
    position: relative; border-radius: 28px; height: 292px; overflow: hidden;
    padding: 26px 22px 20px; color: var(--white);
  }
  .feature-card + .feature-card { margin-top: 16px; }
  .feature-bg { position: absolute; inset: 0; z-index: 0; }
  .transfer-card .feature-bg {
    background: radial-gradient(circle at 78% 28%, rgba(90,160,240,.45), transparent 55%),
                linear-gradient(160deg, var(--card-blue) 0%, var(--card-blue-deep) 100%);
  }
  .token-card .feature-bg {
    background: radial-gradient(circle at 80% 85%, rgba(120,40,140,.55), transparent 45%),
                radial-gradient(circle at 70% 30%, rgba(70,80,160,.35), transparent 50%),
                linear-gradient(160deg, var(--navy) 0%, var(--navy-deep) 100%);
  }
  .feature-body { position: relative; z-index: 1; }
  .feature-title { font-size: 27px; font-weight: 700; letter-spacing: .2px; }
  .feature-lead { font-size: 11.5px; font-weight: 500; line-height: 1.45; margin-top: 8px; max-width: 290px; }
  .tag-row { display: flex; gap: 8px; margin-top: 10px; }
  .tag {
    background: var(--tag-blue); color: var(--white); font-size: 10px; font-weight: 500;
    padding: 4px 12px; border-radius: 6px;
  }
  .action-row { display: flex; gap: 12px; margin-top: 20px; }
  .token-card .action-row { margin-top: 40px; }
  .action { width: 94px; display: flex; flex-direction: column; align-items: center; }
  .action-tile {
    width: 94px; height: 94px; background: var(--white); border-radius: 14px;
    display: flex; align-items: center; justify-content: center;
    box-shadow: 0 6px 14px rgba(0,0,0,.18);
  }
  .action-tile svg { width: 46px; height: 46px; }
  .action-label {
    margin-top: 10px; font-size: 12.5px; font-weight: 600; line-height: 1.2; text-align: center;
  }

  .tab-bar {
    position: absolute; left: 14px; right: 14px; bottom: 0; height: 84px;
    background: var(--white); border-radius: 26px 26px 0 0;
    display: flex; align-items: center; justify-content: space-around; padding: 0 18px 6px;
  }
  .tab-bar svg { width: 30px; height: 30px; }
  .tab-primary {
    width: 44px; height: 44px; border-radius: 50%; background: var(--action-blue);
    display: flex; align-items: center; justify-content: center;
  }
  .tab-primary svg { width: 26px; height: 26px; }
</style>
</head>
<body>
<main class="stage">

  <section class="screen splash" aria-label="Splash screen">
    <div class="splash-mark">
      <span class="splash-dot"></span>
      <span class="splash-name">Veltrano Orbis<br>Wallet</span>
    </div>
  </section>

  <section class="screen home" aria-label="Home screen">

    <article class="feature-card transfer-card">
      <div class="feature-bg" role="img" aria-label="Soft blue illustration of a money transfer on a phone"></div>
      <div class="feature-body">
        <h2 class="feature-title">Money Transfer</h2>
        <p class="feature-lead">Fast doesn't mean expensive. Send money internationally at best rates.</p>
        <div class="tag-row">
          <span class="tag">Low-cost</span>
          <span class="tag">Instant</span>
        </div>
        <div class="action-row">
          <div class="action">
            <div class="action-tile">
              <svg viewBox="0 0 48 48" fill="none" stroke="var(--ink)" stroke-width="2.4" stroke-linecap="round">
                <path d="M10 30a15 15 0 1 1 6 9"/>
                <path d="M10 24v7h7"/>
                <circle cx="24" cy="22" r="6" fill="var(--ink)"/>
                <ellipse cx="18" cy="36" rx="4" ry="1.6"/>
                <ellipse cx="18" cy="39.5" rx="4" ry="1.6"/>
              </svg>
            </div>
            <span class="action-label">Buy<br>Crypto</span>
          </div>
          <div class="action">
            <div class="action-tile">
              <svg viewBox="0 0 48 48" fill="none" stroke="var(--ink)" stroke-width="2.4" stroke-linecap="round">
                <circle cx="29" cy="20" r="11"/>
                <path d="M32 15.5c-1-1-2-1.5-3.5-1.5-2 0-3.5 1-3.5 2.8 0 3.8 7.5 2 7.5 5.8 0 1.8-1.6 2.9-3.8 2.9-1.6 0-3-.6-4-1.7M29 12v2M29 26v2"/>
                <path d="M6 28h12M9 33h10M12 38h8"/>
              </svg>
            </div>
            <span class="action-label">Send<br>Money</span>
          </div>
          <div class="action">
            <div class="action-tile">
              <svg viewBox="0 0 48 48" fill="none" stroke="var(--ink)" stroke-width="2.4" stroke-linecap="round" stroke-linejoin="round">
                <rect x="18" y="10" width="24" height="18" rx="2"/>
                <path d="M18 16h24M22 22h10M22 25h6"/>
                <path d="M10 20v18M5 33l5 5 5-5"/>
              </svg>
            </div>
            <span class="action-label">Withdraw<br>to Card</span>
          </div>
        </div>
      </div>
    </article>

    <article class="feature-card token-card">
      <div class="feature-bg" role="img" aria-label="Dark navy digital backdrop with faint glowing data lines"></div>
      <div class="feature-body">
        <h2 class="feature-title">ORBT Token</h2>
        <p class="feature-lead">The token that makes everything possible.<br>Learn all about it.</p>
        <div class="action-row">
          <div class="action">
            <div class="action-tile">
              <svg viewBox="0 0 48 48" fill="none" stroke="var(--ink)" stroke-width="2.6" stroke-linecap="round">
                <circle cx="24" cy="24" r="15"/>
                <path d="M24 22v9"/>
                <circle cx="24" cy="16.5" r="1" fill="var(--ink)"/>
              </svg>
            </div>
            <span class="action-label">About ORBT</span>
          </div>
          <div class="action">
            <div class="action-tile">
              <svg viewBox="0 0 48 48" fill="none" stroke="var(--ink)" stroke-width="2.4" stroke-linecap="round">
                <path d="M24 8v32M8 24h32"/>
              </svg>
            </div>
            <span class="action-label">Buy ORBT</span>
          </div>
          <div class="action">
            <div class="action-tile">
              <svg viewBox="0 0 48 48">
                <path fill="var(--ink)" d="M25 6c2 7 12 11 12 22a13 13 0 0 1-26 0c0-5 3-9 6-11-1 4 1 7 3 8-1-8 3-14 5-19z"/>
              </svg>
            </div>
            <span class="action-label">What's Hot</span>
          </div>
        </div>
      </div>
    </article>

    <nav class="tab-bar" aria-label="Main navigation">
      <svg viewBox="0 0 32 32" fill="none" stroke="var(--icon-grey)" stroke-width="1.6">
        <rect x="5" y="5" width="9" height="9" rx="1.5"/><rect x="18" y="5" width="9" height="9" rx="1.5"/>
        <rect x="5" y="18" width="9" height="9" rx="1.5"/><rect x="18" y="18" width="9" height="9" rx="1.5"/>
      </svg>
      <svg viewBox="0 0 32 32" fill="none" stroke="var(--icon-grey)" stroke-width="1.6" stroke-linecap="round">
        <rect x="3" y="7" width="26" height="18" rx="2"/><path d="M3 12h26M7 20h8M7 17h5"/>
        <circle cx="23" cy="18.5" r="2.5"/>
      </svg>
      <svg viewBox="0 0 32 32" fill="none" stroke="var(--icon-grey)" stroke-width="1.6" stroke-linejoin="round">
        <path d="M4 15 28 5 20 28l-5-9z"/><path d="M15 19 28 5"/>
      </svg>
      <span class="tab-primary">
        <svg viewBox="0 0 32 32" fill="none" stroke="var(--white)" stroke-width="1.8" stroke-linecap="round">
          <path d="M25 16a9 9 0 1 1-3-6.7"/><path d="M22 5v4.5h-4.5"/><path d="M12 16l3 3 5-5"/>
        </svg>
      </span>
    </nav>

  </section>
</main>
</body>
</html>
```